PlayerMetricsHubOnline - Game Statistics and Achievement Tracking

I need a new modern design for an existing website.

The website is a project to track statistics and achievements for games (currently Vaporo Achievements/Stats and stats for Continental Hauler Pro 2 and Prairie Freight Commander).
I am currently expanding the site with other platforms (like QLV) and more games.
I am also adding a user registration/signin with user profiles to show off their achievements and stats across all platforms and games.

The current website is available at https://plymetrx.example/
To search for data you can use the username "pixeldorian" (without quotes).

The design should be modern and extendable and contain space for a logo.

The logo should match the project. It should combine Gaming with statistics.

Target Market(s)

Video game players

Number of Pages Required

5+ page

Font styles to use
Sans Serif

Requirements
Must have
• Basic Layout, User profile page (not yet available on live site), Search Page for Platforms/Games, Platform profile page, Dark theme

```html
<!DOCTYPE html>
<html lang="en">
<head>
<meta charset="utf-8">
<title>PlayerMetricsHubOnline</title>
<link rel="stylesheet" href="https://fonts.googleapis.com/css2?family=Oswald:wght@400;500;600&family=Nunito:wght@400;500;600&display=swap">
<style>
:root{
  --orange:#f7a20c;
  --orange-deep:#e38f00;
  --black:#000;
  --panel:#111215;
  --white:#fff;
  --muted:#cfcfcf;
  --head:'Oswald',sans-serif;
  --body:'Nunito',sans-serif;
}
*{margin:0;padding:0;box-sizing:border-box}
html,body{width:1200px;height:3464px;overflow:hidden;background:var(--black);color:var(--white);font-family:var(--body)}
.abs{position:absolute}
a{color:inherit;text-decoration:none}

/* header */
.site-header{left:0;top:0;width:1200px;height:85px;background:#050505}
.brand{display:flex;align-items:center;gap:10px}
.brand-dot{width:60px;height:60px;border-radius:50%;background:var(--orange)}
.brand-name{font-family:var(--head);font-weight:500;color:var(--orange);font-size:22px}
.site-header .brand{left:114px;top:12px}
.main-nav{left:499px;top:30px;display:flex;gap:0;font-family:var(--head);font-size:17px}
.main-nav a{padding:0 24px}
.main-nav .sep{color:var(--white)}
.main-nav a.active{color:var(--orange)}
.btn{background:var(--orange);color:var(--white);font-family:var(--head);font-weight:500;border-radius:24px;display:flex;align-items:center;justify-content:center}
.signup{left:970px;top:23px;width:118px;height:47px;font-size:18px}

/* hero */
.hero{left:0;top:85px;width:1200px;height:496px;background:radial-gradient(ellipse at 50% 55%,#1d3550 0%,#0d1a2a 45%,#05070b 90%)}
.hero-title{left:0;top:195px;width:1200px;text-align:center;font-family:var(--head);font-weight:500;font-size:45px;line-height:40px;text-transform:uppercase}
.hero-copy{left:300px;top:328px;width:600px;text-align:center;font-size:15px;line-height:31px}
.register{left:534px;top:408px;width:132px;height:45px;font-size:17px}

/* profile */
.profile{left:112px;top:667px;width:976px;height:396px;background:var(--panel)}
.avatar{left:151px;top:702px;width:398px;height:324px;background:linear-gradient(160deg,#3fa0e6,#2b6db3 40%,#5aa36b);border:3px solid #4fc3ff}
.stats-list{left:588px;top:712px;list-style:none}
.stats-list li{display:flex;align-items:center;height:44px}
.stats-list .label{font-family:var(--head);font-size:19px;width:140px}
.stats-list .value{display:flex;align-items:center;gap:9px;font-size:17px}
.stats-list svg{width:20px;height:20px}
.badge-5{background:var(--orange);color:#fff;font-size:14px;width:22px;height:20px;display:inline-flex;align-items:center;justify-content:center;border-radius:3px}

/* section headings */
.section-title{left:0;width:1200px;text-align:center;font-family:var(--head);font-weight:500;font-size:32px;text-transform:uppercase}
.section-title::after{content:"";display:block;width:50px;height:3px;background:var(--orange);margin:8px auto 0}

/* platforms */
.platforms{left:110px;top:1147px;width:1090px;height:785px;background:linear-gradient(135deg,#0a0a0a,#1e1e1e 50%,#0c0c0c)}
.search{left:191px;top:1294px;width:818px;height:47px;border-radius:24px;background:#2a2a2a;display:flex;align-items:center;justify-content:space-between;padding:0 14px 0 33px;font-size:15px}
.search-icon{width:31px;height:31px;border:2px solid var(--orange);border-radius:50%;display:flex;align-items:center;justify-content:center}
.games-box{left:110px;top:1377px;width:980px;height:471px;border:2px solid var(--white);border-radius:8px}
.game-card{width:292px}
.game-art{width:292px;height:113px}
.view-more{width:206px;height:31px;margin:19px auto 0;font-size:16px;border-radius:2px}

/* statistics */
.statistics{left:0;top:1932px;width:1200px;height:425px;background:#000}
.stat{width:220px;text-align:center}
.stat-ring{width:108px;height:108px;border-radius:50%;background:#2a1d05;margin:0 auto;display:flex;align-items:center;justify-content:center}
.stat-core{width:80px;height:80px;border-radius:50%;background:var(--orange);display:flex;align-items:center;justify-content:center}
.stat-name{font-family:var(--head);font-weight:500;font-size:22px;margin-top:18px;text-transform:uppercase}
.stat-num{font-size:16px;margin-top:4px}
.arrow{width:24px;height:36px}

/* users */
.users{left:0;top:2357px;width:1200px;height:517px;background:linear-gradient(180deg,#0d0d0d,#1a1a1a)}
.user-card{width:306px;text-align:center}
.user-art{width:306px;height:297px;border-radius:8px}
.user-name{font-family:var(--head);font-weight:500;font-size:22px;margin-top:24px}

/* footer */
.footer-brand{left:478px;top:3080px}
.footer-brand .brand-dot{width:80px;height:80px}
.footer-brand .brand-name{font-size:22px}
.footer-nav{left:0;top:3190px;width:1200px;display:flex;justify-content:center;font-family:var(--head);font-size:17px}
.footer-nav a{padding:0 26px}
.contacts{left:110px;top:3252px;width:980px;height:78px;border:1px solid #555;display:flex}
.contact{flex:1;display:flex;align-items:center;justify-content:center;gap:12px;font-size:15px;border-right:1px solid #555}
.contact:last-child{border-right:none}
.contact-icon{width:36px;height:36px;border-radius:50%;background:var(--orange);display:flex;align-items:center;justify-content:center}
.copyright{left:0;top:3373px;width:1200px;text-align:center;font-size:15px}
</style>
</head>
<body>

<header class="site-header abs">
  <div class="brand abs"><span class="brand-dot"></span><span class="brand-name">PlayerMetricsHubOnline</span></div>
  <nav class="main-nav abs">
    <a class="active" href="#">HOME</a><span class="sep">|</span>
    <a href="#">ABOUT US</a><span class="sep">|</span>
    <a href="#">VAPORO</a><span class="sep">|</span>
    <a href="#">GAMES</a>
  </nav>
  <a class="btn signup abs" href="#">SIGN UP</a>
</header>

<section class="hero abs" role="img" aria-label="Dark blue digital data tunnel background"></section>
<h1 class="hero-title abs">Unleashing the power of data for<br>gamers and developers!</h1>
<p class="hero-copy abs">Lorem ipsum dolor sit amet, consectetur adipiscing elit, sed do eiusmod tempor incididunt ut labore et dolore magna aliqua.</p>
<a class="btn register abs" href="#">REGISTER</a>

<section class="profile abs"></section>
<div class="avatar abs" role="img" aria-label="User avatar artwork for pixeldorian"></div>
<ul class="stats-list abs">
  <li><span class="label">Played Games:</span><span class="value"><svg viewBox="0 0 20 20" fill="none" stroke="#fff" stroke-width="1.6"><path d="M3 5h2M3 10h2M3 15h2M8 5h10M8 10h10M8 15h10"/></svg>1166 / 1644 (70%)</span></li>
  <li><span class="label">Total play time:</span><span class="value"><svg viewBox="0 0 20 20" fill="none" stroke="#fff" stroke-width="1.6"><circle cx="10" cy="10" r="8" stroke-dasharray="3 2"/><path d="M10 5v5l3 2"/></svg>1 year 2 months 11 hours 25 minutes</span></li>
  <li><span class="label">Achievements:</span><span class="value"><svg viewBox="0 0 20 20" fill="none" stroke="#fff" stroke-width="1.6"><circle cx="10" cy="8" r="6"/><circle cx="10" cy="8" r="3"/><path d="M6 13l-1 6 5-2 5 2-1-6"/></svg>18007 / 63070 (28%)</span></li>
  <li><span class="label">Member since:</span><span class="value"><svg viewBox="0 0 20 20" fill="none" stroke="#fff" stroke-width="1.6"><rect x="3" y="4" width="14" height="13"/><path d="M3 8h14M7 2v4M13 2v4"/></svg>14.01.2009</span></li>
  <li><span class="label">Last played:</span><span class="value"><span class="badge-5">5</span>Rail Conductor Sim 5</span></li>
  <li><span class="label">Last Update:</span><span class="value"><svg viewBox="0 0 20 20" fill="none" stroke="#fff" stroke-width="1.6"><path d="M16 8a6 6 0 0 0-11-2M4 12a6 6 0 0 0 11 2M5 2v4h4M15 18v-4h-4"/></svg>26.12.2024 14:11h</span></li>
</ul>

<section class="platforms abs"></section>
<h2 class="section-title abs" style="top:1212px">Platforms/Games</h2>
<div class="search abs"><span>SEARCH GAME</span><span class="search-icon"><svg width="12" height="12" viewBox="0 0 12 12" fill="none" stroke="#f7a20c" stroke-width="1.5"><circle cx="5" cy="5" r="3.5"/><path d="M8 8l3 3"/></svg></span></div>
<div class="games-box abs"></div>
<div class="game-card abs" style="left:136px;top:1420px"><div class="game-art" role="img" aria-label="Grid Logic game cover" style="background:linear-gradient(120deg,#6a3fc8,#2c9be0,#8a3fb5)"></div><a class="btn view-more" href="#">VIEW MORE</a></div>
<div class="game-card abs" style="left:454px;top:1420px"><div class="game-art" role="img" aria-label="Lunar Drift game cover" style="background:linear-gradient(120deg,#6b4a3b,#e9d2bd,#2f3b6b)"></div><a class="btn view-more" href="#">VIEW MORE</a></div>
<div class="game-card abs" style="left:771px;top:1420px"><div class="game-art" role="img" aria-label="Dread Manor 2 game cover" style="background:linear-gradient(120deg,#1f2a3a,#3a3f4a,#5a1a1a)"></div><a class="btn view-more" href="#">VIEW MORE</a></div>
<div class="game-card abs" style="left:136px;top:1625px"><div class="game-art" role="img" aria-label="Cannon Crew game cover" style="background:linear-gradient(120deg,#3a7fc8,#d28a3a,#8a4a2a)"></div><a class="btn view-more" href="#">VIEW MORE</a></div>
<div class="game-card abs" style="left:454px;top:1625px"><div class="game-art" role="img" aria-label="Nasty Neighbours game cover" style="background:linear-gradient(120deg,#7a4a20,#c07a2a,#6a3a15)"></div><a class="btn view-more" href="#">VIEW MORE</a></div>
<div class="game-card abs" style="left:771px;top:1625px"><div class="game-art" role="img" aria-label="Dwelling game cover" style="background:linear-gradient(120deg,#15120e,#2b2418,#15120e)"></div><a class="btn view-more" href="#">VIEW MORE</a></div>

<section class="statistics abs"></section>
<h2 class="section-title abs" style="top:2003px">Statistics</h2>
<svg class="arrow abs" style="left:44px;top:2156px" viewBox="0 0 24 36" fill="none" stroke="#fff" stroke-width="2.5"><path d="M18 4L6 18l12 14"/></svg>
<svg class="arrow abs" style="left:1132px;top:2156px" viewBox="0 0 24 36" fill="none" stroke="#fff" stroke-width="2.5"><path d="M6 4l12 14L6 32"/></svg>
<div class="stat abs" style="left:53px;top:2086px"><div class="stat-ring"><div class="stat-core"><svg width="36" height="24" viewBox="0 0 36 24" fill="none" stroke="#3a2600" stroke-width="2"><path d="M8 3h20a6 6 0 0 1 6 6l1 9a4 4 0 0 1-7 2l-3-4H11l-3 4a4 4 0 0 1-7-2l1-9a6 6 0 0 1 6-6z"/><path d="M10 8v6M7 11h6"/><circle cx="25" cy="9" r="1"/><circle cx="28" cy="12" r="1"/></svg></div></div><div class="stat-name">Games</div><div class="stat-num">251966</div></div>
<div class="stat abs" style="left:244px;top:2086px"><div class="stat-ring"><div class="stat-core"><svg width="36" height="24" viewBox="0 0 36 24" fill="none" stroke="#3a2600" stroke-width="2"><path d="M8 3h20a6 6 0 0 1 6 6l1 9a4 4 0 0 1-7 2l-3-4H11l-3 4a4 4 0 0 1-7-2l1-9a6 6 0 0 1 6-6z"/><path d="M10 8v6M7 11h6"/><circle cx="25" cy="9" r="1"/><circle cx="28" cy="12" r="1"/></svg></div></div><div class="stat-name">Game Achievements</div><div class="stat-num">251966</div></div>
<div class="stat abs" style="left:460px;top:2086px"><div class="stat-ring"><div class="stat-core"><svg width="36" height="24" viewBox="0 0 36 24" fill="none" stroke="#3a2600" stroke-width="2"><path d="M8 3h20a6 6 0 0 1 6 6l1 9a4 4 0 0 1-7 2l-3-4H11l-3 4a4 4 0 0 1-7-2l1-9a6 6 0 0 1 6-6z"/><path d="M10 8v6M7 11h6"/><circle cx="25" cy="9" r="1"/><circle cx="28" cy="12" r="1"/></svg></div></div><div class="stat-name">Game Stats</div><div class="stat-num">251966</div></div>
<div class="stat abs" style="left:669px;top:2086px"><div class="stat-ring"><div class="stat-core"><svg width="36" height="24" viewBox="0 0 36 24" fill="none" stroke="#3a2600" stroke-width="2"><path d="M8 3h20a6 6 0 0 1 6 6l1 9a4 4 0 0 1-7 2l-3-4H11l-3 4a4 4 0 0 1-7-2l1-9a6 6 0 0 1 6-6z"/><path d="M10 8v6M7 11h6"/><circle cx="25" cy="9" r="1"/><circle cx="28" cy="12" r="1"/></svg></div></div><div class="stat-name">Playtime Records</div><div class="stat-num">251966</div></div>
<div class="stat abs" style="left:904px;top:2086px"><div class="stat-ring"><div class="stat-core"><svg width="36" height="24" viewBox="0 0 36 24" fill="none" stroke="#3a2600" stroke-width="2"><path d="M8 3h20a6 6 0 0 1 6 6l1 9a4 4 0 0 1-7 2l-3-4H11l-3 4a4 4 0 0 1-7-2l1-9a6 6 0 0 1 6-6z"/><path d="M10 8v6M7 11h6"/><circle cx="25" cy="9" r="1"/><circle cx="28" cy="12" r="1"/></svg></div></div><div class="stat-name">Public Profiles</div><div class="stat-num">251966</div></div>

<section class="users abs"></section>
<h2 class="section-title abs" style="top:2420px">Our Users</h2>
<div class="user-card abs" style="left:112px;top:2525px"><div class="user-art" role="img" aria-label="Phone with casino game among poker chips" style="background:linear-gradient(135deg,#7a1a1a,#1f4a3a 55%,#0f2a40)"></div><div class="user-name">LOREM IPSUM DOLOR</div></div>
<div class="user-card abs" style="left:447px;top:2525px"><div class="user-art" role="img" aria-label="Isometric gaming setup in neon blue" style="background:linear-gradient(135deg,#1a2a8a,#3a5ad8 50%,#7a2a9a)"></div><div class="user-name">LOREM IPSUM DOLOR</div></div>
<div class="user-card abs" style="left:783px;top:2525px"><div class="user-art" role="img" aria-label="Hand holding phone with sports stats in front of laptop" style="background:linear-gradient(135deg,#3a3a2a,#5a8a3a 50%,#d8d8d8)"></div><div class="user-name">LOREM IPSUM DOLOR</div></div>

<footer>
  <div class="brand footer-brand abs"><span class="brand-dot"></span><span class="brand-name">PlayerMetricsHubOnline</span></div>
  <nav class="footer-nav abs">
    <a href="#">Home</a>|<a href="#">About Us</a>|<a href="#">Vaporo</a>|<a href="#">Games</a>|<a href="#">Contact Us</a>
  </nav>
  <div class="contacts abs">
    <div class="contact"><span class="contact-icon"><svg width="16" height="16" viewBox="0 0 16 16" fill="#fff"><path d="M3 1l3 3-1.5 2a9 9 0 0 0 5.5 5.5L12 10l3 3-2 2C7 15 1 9 1 3z"/></svg></span>+1 555 0142 7788</div>
    <div class="contact"><span class="contact-icon"><svg width="16" height="12" viewBox="0 0 16 12" fill="#fff"><path d="M0 0h16v12H0z"/><path d="M0 0l8 6 8-6" stroke="#f7a20c" fill="none" stroke-width="1.5"/></svg></span>info@plymetrx.example</div>
    <div class="contact"><span class="contact-icon"><svg width="14" height="18" viewBox="0 0 14 18" fill="#fff"><path d="M7 0a7 7 0 0 1 7 7c0 5-7 11-7 11S0 12 0 7a7 7 0 0 1 7-7z"/><circle cx="7" cy="7" r="2.5" fill="#f7a20c"/></svg></span>PlayerMetricsHubOnline, United States</div>
  </div>
  <p class="copyright abs">Copyrights@2024.PlayerMetricsHubOnline.All Rights Reserved</p>
</footer>

</body>
</html>
```